Brookhaven Commerce Park Media Package

We are looking for a designer to unify our company's image throughout its stationery and marketing deliverables. We will be focusing on:
*Business Cards (3.5 x 2)
*Letter Head (Letter Size)
*PowerPoint Presentation Template,
*One Pager Flyer (Letter Size)
*Front of Elevator's bay: 4 photos of the elevator bays (two groups of 3 elevators) to which we are looking for designs for its doors and surrounding wall (vinyl prints)
*Font's suggestions
*Official color palette.
*Outdoor Street Signage: please use the following dimensions:
Sign #1 (Galloway Side): 48(W)x72"(H) (3 sided)
Sign #2: 24"(W)x48"(H) (3 sided)
Sign #3 (Top of Hill): 30(W)x54(H) (2 sides)
*Carport Sign:
See photos attached. The white letters will be removed, and a new sign will take place. Preferably, Cut-Out fonts, but we can consider an alternative approach for cost effective solution.
Find attached the approved logos.
______________________________________
We are a real estate holding company focused on the commercial office space in the Ohio, US, market.
You can check our site at www.brookhavenpark.example
As inspiration guidelines, we would like to see designs that are modern, minimalistic, dynamic and energetic.
Target Market(s)
General Population, Business Owners, Non-Profit Organizations, Government
Industry/Entity Type
Real Estate - Commercial Office Space - Flex Space

```html
<!DOCTYPE html>
<html lang="en">
<head>
<meta charset="utf-8">
<title>Brookhaven Commerce Park Letterhead</title>
<link href="https://fonts.googleapis.com/css2?family=Figtree:wght@400;500;600;700;800&family=Montserrat:wght@700&display=swap" rel="stylesheet">
<style>
  :root {
    --navy: #1a2340;
    --ink: #222222;
    --brand-blue: #1b9ad6;
    --rule-blue: #1f6fb0;
    --footer-navy: #1c2b6b;
    --icon-a: #12a6dc;
    --icon-b: #0a86c6;
    --band-start: #00aee0;
    --band-end: #0b71ad;
    --watermark: #e6e6e6;
    --paper: #ffffff;
  }
  * { margin: 0; padding: 0; box-sizing: border-box; }
  html, body { width: 964px; height: 1200px; overflow: hidden; background: var(--paper); }
  .letterhead {
    position: relative; width: 964px; height: 1200px; overflow: hidden;
    background: var(--paper); font-family: "Figtree", sans-serif; color: var(--ink);
  }
  .brand { position: absolute; left: 64px; top: 34px; display: flex; align-items: center; gap: 12px; }
  .brand-mark { width: 74px; height: 74px; border: 2px solid var(--brand-blue); border-radius: 50%; }
  .brand-name { font-weight: 800; font-size: 27px; line-height: 1; color: var(--navy); letter-spacing: 0.5px; }
  .brand-name span { display: block; font-size: 27px; }
  .header-rule { position: absolute; left: 363px; right: 0; top: 70px; height: 2px; background: var(--rule-blue); }
  .watermark {
    position: absolute; left: 637px; top: 650px; width: 480px; height: 480px;
    border-radius: 50%; background: var(--watermark);
  }
  .recipient { position: absolute; left: 81px; top: 222px; font-size: 14px; font-weight: 500; line-height: 30px; }
  .recipient .label { display: inline-block; width: 27px; }
  .date { position: absolute; left: 654px; top: 304px; font-size: 14px; font-weight: 500; }
  .body { position: absolute; left: 81px; top: 379px; width: 810px; font-size: 14.2px; font-weight: 500; line-height: 27px; }
  .body p { margin-bottom: 27px; }
  .signature { position: absolute; left: 84px; top: 856px; width: 170px; height: 56px; background: #f1f1f1; border-radius: 4px; }
  .signer { position: absolute; left: 85px; top: 914px; }
  .signer-name { font-size: 17px; font-weight: 700; }
  .signer-role { font-size: 13.5px; font-weight: 500; margin-top: 10px; }
  .contact { position: absolute; top: 1113px; display: flex; align-items: center; gap: 21px; font-family: "Montserrat", sans-serif; font-weight: 700; font-size: 14.5px; line-height: 17px; color: var(--footer-navy); }
  .contact-icon { width: 39px; height: 39px; border-radius: 4px; background: linear-gradient(135deg, var(--icon-a), var(--icon-b)); display: flex; align-items: center; justify-content: center; }
  .contact-icon svg { width: 22px; height: 22px; }
  .contact--phone { left: 143px; }
  .contact--address { left: 362px; }
  .contact--mail { left: 669px; }
  .bottom-band { position: absolute; left: 0; right: 0; bottom: 0; height: 24px; background: linear-gradient(90deg, var(--band-start), var(--band-end)); }
</style>
</head>
<body>
<main class="letterhead">
  <div class="watermark" aria-hidden="true"></div>

  <header class="brand">
    <div class="brand-mark" aria-hidden="true"></div>
    <div class="brand-name">BROOKHAVEN<span>COMMERCE PARK</span></div>
  </header>
  <div class="header-rule"></div>

  <section class="recipient">
    <div>Marcus Hale</div>
    <div>Chief Director</div>
    <div><span class="label">A :</span> 45-1, Your Address here - 8989</div>
    <div><span class="label">W :</span> hello@brookhavenpark.example, www.brookhavenpark.example</div>
    <div><span class="label">P :</span> +123 - 12345 - 6789</div>
  </section>
  <div class="date">Date: 10 September, 2022</div>

  <article class="body">
    <p>This is a sample letter that has been placed to demonstrate typing remat (Your Company). letterhead design. When positioned properly, it will serve to work in harmony with all other elements letterhead. This letterhead design is meant to project an image</p>
    <p>This letterhead design is meant project an image of professionalism reliability. By using simple aligen we have created a very spacious feeling. The simplicity suggest rengththe spaciousnes contributes h aesthetics the layout. These basic qualities along with the (Your Company)</p>
    <p>look and helps reinforce the (Your Company) brand. letterhead design is meant to project an image p design. When positioned properly, it will serve to work in harmony all the other elements letterhead. sionalism and reliability.</p>
    <p>This letterhead design is based on the (Form of your logo) form (Your Company) logo. Each stationery we have created a very spacious feeling. The simplicity suggests strength the spaciousnes contribute part of the (Form of your logo).</p>
  </article>

  <div class="signature" role="img" aria-label="Handwritten signature of Daniel Whitford"></div>
  <div class="signer">
    <div class="signer-name">Daniel Whitford</div>
    <div class="signer-role">Manager</div>
  </div>

  <div class="contact contact--phone">
    <div class="contact-icon"><svg viewBox="0 0 24 24" fill="#fff"><path d="M6.6 10.8a15.1 15.1 0 0 0 6.6 6.6l2.2-2.2a1 1 0 0 1 1-.25 11.4 11.4 0 0 0 3.6.57 1 1 0 0 1 1 1V20a1 1 0 0 1-1 1A17 17 0 0 1 3 4a1 1 0 0 1 1-1h3.5a1 1 0 0 1 1 1c0 1.25.2 2.45.57 3.57a1 1 0 0 1-.25 1z"/></svg></div>
    <div>216-555-0143</div>
  </div>
  <div class="contact contact--address">
    <div class="contact-icon"><svg viewBox="0 0 24 24" fill="#fff"><path d="M12 2a7 7 0 0 0-7 7c0 5.2 7 13 7 13s7-7.8 7-13a7 7 0 0 0-7-7zm0 9.5A2.5 2.5 0 1 1 12 6.5a2.5 2.5 0 0 1 0 5z"/></svg></div>
    <div>4800 Galloway Road,<br>Galloway OH 43119</div>
  </div>
  <div class="contact contact--mail">
    <div class="contact-icon"><svg viewBox="0 0 24 24" fill="none" stroke="#fff" stroke-width="2"><rect x="3" y="5" width="18" height="14" rx="2" fill="#fff" stroke="none"/><path d="M4 7l8 6 8-6" stroke="#0a86c6"/></svg></div>
    <div>Put Your<br>Mail Here</div>
  </div>

  <div class="bottom-band"></div>
</main>
</body>
</html>
```